依頼概要
■依頼の目的/概要
コンサルティング業の中で「ほたる相談室」というテーマの中で、
営業力や対人対応力の向上支援などをお手伝いしています。
今回電子書籍出版にあたり、添付ファイルの書籍のイメージに沿うデザインを製作依頼させていただきます。

■書籍タイトル:『どうして?腕時計を磨くと来店客がふえるのか』
サブタイトル:「未来をひらくのは話術より笑顔力」

■本の内容
見た目が人に与える印象などについて記載したものになります。
営業マンのような個人の方や、法人教育に携わるような方にもお読みいただきたいものです。
詳細は添付ファイルを参照ください。

■デザイン要望
自由なご提案をおまちしております。
堅苦しくなく、気軽に手に取っていただけるようなデザインを希望です。

その他何かご不明な点がございましたら、お気軽にご質問下さい。
よろしくお願いいたします。
提案して頂いた皆様、私のミスで写真を2枚お送りできていませんでした。
大変申し訳ございませんがこの写真2枚を使って頂けますよう宜しくお願い致します。

この写真を使ってください
■ 選んだ理由

ネクタイの縦とメッセージの流れがとても良かったです。

■ 提案者全員のお礼・コメント

今回は、沢山の人にいろいろなデザインでご提案いただきありがとうございました。

```html
<!DOCTYPE html>
<html lang="ja">
<head>
<meta charset="utf-8">
<title>どうして？腕時計を磨くと来店客がふえるのか？</title>
<link href="https://fonts.googleapis.com/css2?family=Noto+Sans+JP:wght@500;700;900&display=swap" rel="stylesheet">
<style>
:root{
  --frame:#f7c500;
  --paper:#ffffff;
  --ink:#222222;
  --accent:#e8343b;
  --tag:#4a4a4a;
  --present:#f0a21a;
  --tone-pink:#f7b3c8;
  --tone-grey:#b9c3c9;
  --tone-orange:#f8c066;
  --tone-blue:#8fb7e3;
  --tone-red:#ef8a96;
  --tone-green:#a9d98c;
  --tone-sky:#9fd3ee;
}
*{margin:0;padding:0;box-sizing:border-box}
html,body{width:750px;height:1200px;overflow:hidden;background:var(--frame)}
body{font-family:"Noto Sans JP",sans-serif;color:var(--ink)}
.cover{position:relative;width:750px;height:1200px;background:var(--frame);padding:20px 20px 0}
.sheet{position:relative;width:710px;height:975px;background:var(--paper);padding-top:38px}
.tagline{text-align:center;font-size:34px;font-weight:700;letter-spacing:1px;line-height:1.2}
.tagline .em{color:var(--accent);position:relative}
.tagline .em::before{content:"・・・";position:absolute;left:0;right:0;top:-22px;text-align:center;font-size:28px;letter-spacing:6px;color:var(--accent)}
.rule{width:640px;height:3px;background:var(--ink);margin:18px auto 0}
.title{margin:26px auto 0;width:670px;font-size:80px;font-weight:900;line-height:1.2;letter-spacing:2px}
.art{position:absolute;left:20px;right:20px;top:455px;bottom:24px;
  background:linear-gradient(90deg,var(--tone-pink),var(--tone-grey),var(--tone-orange),var(--tone-blue),var(--tone-red),var(--tone-green),var(--tone-sky));
  border-radius:6px;opacity:.85}
.gift{position:absolute;left:0;bottom:0;width:750px;height:205px;display:flex;align-items:center;padding:0 14px 0 0;gap:12px}
.gift-tag{width:112px;height:150px;background:var(--tag);color:#fff;display:flex;flex-direction:column;align-items:center;justify-content:center;clip-path:polygon(0 0,100% 0,100% 84%,50% 100%,0 84%)}
.gift-tag .big{font-size:38px;font-weight:900;color:var(--frame);line-height:1.1}
.gift-tag .small{font-size:19px;font-weight:700;margin-top:6px}
.gift-item{flex:1;height:150px;background:var(--paper);border:3px dotted var(--present);display:flex;flex-direction:column;align-items:center;justify-content:center;text-align:center}
.gift-label{font-size:20px;font-weight:700;color:var(--present);margin-bottom:8px}
.gift-lead{font-size:19px;font-weight:700;line-height:1.3}
.gift-main{font-size:29px;font-weight:900;line-height:1.25}
.gift-tail{font-size:19px;font-weight:700;line-height:1.3}
</style>
</head>
<body>
<div class="cover">
  <div class="sheet">
    <p class="tagline">未来をひらくのは話術より<span class="em">笑顔力</span>!!</p>
    <div class="rule"></div>
    <h1 class="title">どうして？腕時計を磨くと来店客がふえるのか？</h1>
    <div class="art" role="img" aria-label="ピンク・グレー・オレンジ・青・赤・緑など色や柄の異なる品が二段に縦並びするカラフルなイラスト"></div>
  </div>
  <div class="gift">
    <div class="gift-tag"><span class="big">読者</span><span class="small">プレゼント</span></div>
    <div class="gift-item">
      <span class="gift-label">Present ❶</span>
      <span class="gift-lead">得たい成果を得るための</span>
      <span class="gift-main">5つのステップ</span>
      <span class="gift-tail">テンプレート</span>
    </div>
    <div class="gift-item">
      <span class="gift-label">Present ❷</span>
      <span class="gift-lead">マスコミでは出さない</span>
      <span class="gift-main">もの選びのポイント</span>
      <span class="gift-tail">を伝授</span>
    </div>
  </div>
</div>
</body>
</html>
```